Web Design Project for starting CCTV/Camera security installer/reseller

Hello,

An old class mate is starting his own little CCTV/Camera security business as a one-man-gang.

He asked me to do his website but unfortunatly my design skills are not worth looking at :) The coding is no problem.

So I'm here to request a design.

What he wants is a site that lists the products he might install which is based on a small tree structure. So see it as a shop overview/display but without the baskets & cashout options.

you can find a site structure scheme, logo, product images & data sheet pdf's at this filvaultra address:

https://www.filvaultra.com/sh/kq7zt3908wx4pl2/vnRtLoBe5y/Lumo-Ward

the site itself is http://www.lumo-ward.be but only has a splash screen until I have a design for it.

the logo is a bit out of proportions, not sure if you can make something good out of it :/

Most content is in Dutch, I'll see if I can translate the needed parts...
Updates

Dear designers,

I have some good new for you.

You are allowed to use only that chrome Lumo-Ward part of the logo,
which should make things a lot easier to fit into your design ideas.

Keep up the creativity!

Dear designers,

I uploaded a new logo to the filvaultra space.

It's a png but unfortunately it's not transparent, I'm still waiting for that one
but you know how to erase it in photoshop.

Target Market(s)

people looking for a visual solution to protect their company/home

Industry/Entity Type

Security

Requirements
Must have
• an iconized way to browse/display a tree. (not the traditional folder/explorer style)

maybe first a page with buttons/icons showing level 1 the group types (IP cams, IP servers, Accessories)

level 2 product groups (dome cam, ptz cam etc)

level 3 the actual product + a link to a pdf datasheet (if any)

could be multipage or maybe in/on-page since the product list won't be that huge.

maybe some random product info left and/or right so that the content area is not massive since he has not much to type
;)

```html
<!DOCTYPE html>
<html lang="en">
<head>
<meta charset="utf-8">
<title>Lumo-Ward Camera Security Systems</title>
<link rel="stylesheet" href="https://fonts.googleapis.com/css2?family=Open+Sans:wght@400;600;700&display=swap">
<style>
:root{
  --page-bg:#e6e9ec;
  --header-dark:#34373c;
  --header-light:#4a4e54;
  --blue:#2c86d1;
  --blue-dark:#1f6fb4;
  --orange:#f08a1c;
  --text:#4a4a4a;
  --muted:#8a8f95;
  --line:#dde2e7;
  --white:#ffffff;
  --footer:#2f3236;
  --footer-deep:#25282b;
}
*{box-sizing:border-box;margin:0;padding:0}
html,body{width:720px;height:1200px;overflow:hidden}
body{background:var(--page-bg);font-family:"Open Sans",Arial,sans-serif;color:var(--text);position:relative;font-size:8px}
a{text-decoration:none;color:inherit}

.site-header{position:absolute;left:0;top:0;width:720px;height:78px;background:linear-gradient(var(--header-light),var(--header-dark))}
.brand{position:absolute;left:92px;top:20px;display:flex;align-items:center;gap:8px}
.brand-mark{width:16px;height:16px;border-radius:50%;background:var(--blue)}
.brand-name{color:var(--white);font-weight:700;font-size:20px;letter-spacing:.5px}
.brand-tag{position:absolute;left:116px;top:47px;color:#b8bdc3;font-size:7px;letter-spacing:1.5px}
.call{position:absolute;right:88px;top:22px;text-align:right;color:var(--white)}
.call small{display:block;font-size:7px;color:#b8bdc3;letter-spacing:1px}
.call strong{font-size:15px;font-weight:700;letter-spacing:.5px}

.main-nav{position:absolute;left:85px;top:78px;width:550px;height:26px;background:linear-gradient(#3a97e0,var(--blue-dark));display:flex;align-items:center;padding:0 12px;gap:18px}
.main-nav a{color:var(--white);font-size:7.5px;font-weight:600}
.main-nav a.active{background:var(--orange);padding:4px 8px;border-radius:2px}
.search{margin-left:auto;display:flex}
.search span{width:120px;height:15px;background:var(--white);font-size:6.5px;color:var(--muted);padding:3px 5px}
.search i{width:16px;height:15px;background:var(--orange);display:flex;align-items:center;justify-content:center}

.content{position:absolute;left:85px;top:104px;width:550px;height:1012px;background:var(--white)}
.welcome-title{position:absolute;left:18px;top:14px;font-size:11px;font-weight:700;color:#333}
.welcome-photo{position:absolute;left:20px;top:40px;width:120px;height:100px;background:radial-gradient(circle at 50% 45%,#f4f4f4,#c9ced4);border-radius:3px}
.welcome-text{position:absolute;left:160px;top:40px;width:370px}
.welcome-text h2{color:var(--blue);font-size:12px;font-weight:600;line-height:1.3;margin-bottom:8px}
.welcome-text p{font-size:7.5px;line-height:1.55;margin-bottom:6px}

.divider{position:absolute;left:18px;right:18px;top:325px;border-top:1px solid var(--line)}
.browse-title{position:absolute;left:18px;top:338px;font-size:11px;font-weight:700;color:#333}
.tabs{position:absolute;left:40px;top:366px;display:flex;gap:3px}
.tabs a{width:120px;height:20px;background:#b9d6ef;color:var(--white);font-size:7px;font-weight:600;display:flex;align-items:center;justify-content:center}
.tabs a.current{background:var(--blue)}
.catalog{position:absolute;left:40px;top:386px;width:470px;height:540px;border:1px solid var(--line);border-top:3px solid var(--blue);background:#fbfcfd}
.crumb{position:absolute;left:10px;top:10px;font-size:8px;color:#555}
.select{position:absolute;left:10px;top:26px;width:50px;height:13px;border:1px solid #bbb;background:var(--white);font-size:6.5px;padding:2px 4px;white-space:nowrap;overflow:hidden}
.options{position:absolute;left:10px;top:40px;width:100px;background:var(--white);border:1px solid #bbb;z-index:3;list-style:none}
.options li{font-size:6.5px;padding:2px 4px;color:#444}
.options li.hover{background:var(--blue);color:var(--white)}

.grid{position:absolute;left:60px;top:26px;width:400px;display:grid;grid-template-columns:1fr 1fr;gap:8px 10px}
.card{height:112px;background:var(--white);border:1px solid var(--line);position:relative}
.card-photo{position:absolute;left:8px;top:10px;width:70px;height:60px;background:radial-gradient(circle at 50% 55%,#fafafa,#cdd2d8);border-radius:2px}
.card-body{position:absolute;left:86px;top:8px;right:6px}
.card-body h3{color:var(--blue);font-size:8px;font-weight:700;margin-bottom:3px}
.card-body p{font-size:6px;line-height:1.35;color:#666;margin-bottom:3px}
.card-body ul{list-style:none;font-size:6px;color:#666;line-height:1.4}
.details{position:absolute;left:8px;bottom:7px;font-size:6.5px;color:var(--blue);font-weight:600}

.pager{position:absolute;right:40px;top:936px;display:flex;gap:3px}
.pager span{width:12px;height:12px;background:#cfdbe6;font-size:6px;color:var(--white);display:flex;align-items:center;justify-content:center}
.pager span.on{background:var(--blue)}

.site-footer{position:absolute;left:0;top:1116px;width:720px;height:84px;background:var(--footer)}
.foot-col{position:absolute;top:8px;color:#c4c8cd;font-size:6.5px;line-height:1.6}
.foot-col h4{color:var(--white);font-size:7.5px;font-weight:700;margin-bottom:3px}
.newsletter-field{display:flex;margin-top:2px}
.newsletter-field span{width:110px;height:13px;background:var(--white);color:var(--muted);padding:2px 4px}
.newsletter-field i{width:22px;height:13px;background:var(--orange)}
.foot-call{margin-top:4px;text-align:right;width:132px}
.foot-bottom{position:absolute;left:0;bottom:0;width:720px;height:14px;background:var(--footer-deep);color:#9aa0a6;font-size:6px;padding:3px 92px}
</style>
</head>
<body>

<header class="site-header">
  <div class="brand"><span class="brand-mark"></span><span class="brand-name">Lumo-Ward</span></div>
  <div class="brand-tag">CAMERA SECURITY SYSTEMS</div>
  <div class="call"><small>CALL US</small><strong>+32 470 00 12 34</strong></div>
</header>

<nav class="main-nav">
  <a href="#">HOMEPAGE</a>
  <a href="#">TIPS</a>
  <a href="#" class="active">INSTALLATION</a>
  <a href="#">CONTACT</a>
  <div class="search"><span>Search product here...</span><i>
    <svg width="8" height="8" viewBox="0 0 8 8"><circle cx="3.2" cy="3.2" r="2.3" fill="none" stroke="#fff" stroke-width="1"/><line x1="5" y1="5" x2="7.5" y2="7.5" stroke="#fff" stroke-width="1.2"/></svg></i></div>
</nav>

<main class="content">
  <h1 class="welcome-title">Welcome at Lumo-Ward Camera surveillance</h1>
  <div class="welcome-photo" role="img" aria-label="Hands holding a small model house"></div>
  <div class="welcome-text">
    <h2>Are you looking for a camera system<br>for your home or company?</h2>
    <p>Then you are at Lumo-Ward at the right address!</p>
    <p>We offer a large amount of surveillance cameras, video storage systems and surveillance monitors.</p>
    <p>But we also have complete camera surveillance sets for you (analogue or IP camera) including the cables and power supplies, so that you don't have to worry about additional components when ordering.</p>
  </div>
  <div class="divider"></div>

  <h2 class="browse-title">Browse our Products and Found the Best for You</h2>
  <div class="tabs"><a href="#" class="current">IP CAMS</a><a href="#">IP ACCESSORIES</a><a href="#">IP SERVERS</a></div>

  <section class="catalog">
    <div class="crumb">Products &gt; IP Cams &gt; All product</div>
    <div class="select">All products ▾</div>
    <ul class="options">
      <li>All products</li><li>LW-Box Camera</li><li>LW-Bullet</li><li>LW-Cube</li><li>LW-Dome Indoor</li>
      <li class="hover">LW-Dome PoE</li><li>LW-Mini Camera</li><li>LW-Mini Dome Indoor</li><li>LW-Mini Dome Outdoor</li>
      <li>LW-PTZ Dome</li><li>LW-Speed Dome Indoor</li><li>LW-Speed Dome Outdoor</li><li>LW-Vandal Dome</li>
    </ul>

    <div class="grid">
      <article class="card"><div class="card-photo" role="img" aria-label="Bullet camera product photo"></div>
        <div class="card-body"><h3>LW-BL1200</h3><p>Some information about the product. Recommended use: flush, slotted mounts that fit on small panels.</p><ul><li>» 1.3" progressive scan</li><li>» 3 IR Sensors</li><li>» Intelligent IR</li><li>» Up to 30FPS at 1280x1024</li></ul></div>
        <a class="details" href="#">see details »</a></article>
      <article class="card"><div class="card-photo" role="img" aria-label="Dome camera product photo"></div>
        <div class="card-body"><h3>LW-VD1200</h3><p>Some information about the product. Recommended use: flush, slotted mounts that fit on small panels.</p><ul><li>» 1.3 Megapixel</li><li>» 3 IR Sensors</li><li>» Intelligent IR</li><li>» Up to 30FPS at 1280x1024</li></ul></div>
        <a class="details" href="#">see details »</a></article>
      <article class="card"><div class="card-photo" role="img" aria-label="Dome camera product photo"></div>
        <div class="card-body"><h3>LW-VD1200</h3><p>Some information about the product. Recommended use: flush, slotted mounts that fit on small panels.</p><ul><li>» 1.3 Megapixel</li><li>» 3 IR Sensors</li><li>» Intelligent IR</li><li>» Up to 30FPS at 1280x1024</li></ul></div>
        <a class="details" href="#">see details »</a></article>
      <article class="card"><div class="card-photo" role="img" aria-label="Bullet camera product photo"></div>
        <div class="card-body"><h3>LW-BL1200</h3><p>Some information about the product. Recommended use: flush, slotted mounts that fit on small panels.</p><ul><li>» 1.3" progressive scan</li><li>» 3 IR Sensors</li><li>» Intelligent IR</li><li>» Up to 30FPS at 1280x1024</li></ul></div>
        <a class="details" href="#">see details »</a></article>
      <article class="card"><div class="card-photo" role="img" aria-label="Bullet camera product photo"></div>
        <div class="card-body"><h3>LW-BL1200</h3><p>Some information about the product. Recommended use: flush, slotted mounts that fit on small panels.</p><ul><li>» 1.3" progressive scan</li><li>» 3 IR Sensors</li><li>» Intelligent IR</li><li>» Up to 30FPS at 1280x1024</li></ul></div>
        <a class="details" href="#">see details »</a></article>
      <article class="card"><div class="card-photo" role="img" aria-label="Dome camera product photo"></div>
        <div class="card-body"><h3>LW-VD1200</h3><p>Some information about the product. Recommended use: flush, slotted mounts that fit on small panels.</p><ul><li>» 1.3 Megapixel</li><li>» 3 IR Sensors</li><li>» Intelligent IR</li><li>» Up to 30FPS at 1280x1024</li></ul></div>
        <a class="details" href="#">see details »</a></article>
      <article class="card"><div class="card-photo" role="img" aria-label="Dome camera product photo"></div>
        <div class="card-body"><h3>LW-VD1200</h3><p>Some information about the product. Recommended use: flush, slotted mounts that fit on small panels.</p><ul><li>» 1.3 Megapixel</li><li>» 3 IR Sensors</li><li>» Intelligent IR</li><li>» Up to 30FPS at 1280x1024</li></ul></div>
        <a class="details" href="#">see details »</a></article>
      <article class="card"><div class="card-photo" role="img" aria-label="Bullet camera product photo"></div>
        <div class="card-body"><h3>LW-BL1200</h3><p>Some information about the product. Recommended use: flush, slotted mounts that fit on small panels.</p><ul><li>» 1.3" progressive scan</li><li>» 3 IR Sensors</li><li>» Intelligent IR</li><li>» Up to 30FPS at 1280x1024</li></ul></div>
        <a class="details" href="#">see details »</a></article>
    </div>
  </section>
  <div class="pager"><span class="on">1</span><span>2</span><span>3</span><span>»</span></div>
</main>

<footer class="site-footer">
  <div class="foot-col" style="left:92px"><h4>MENU</h4>HOMEPAGE<br>TIPS<br>INSTALLATION<br>CONTACT</div>
  <div class="foot-col" style="left:235px"><h4>CUSTOMER SERVICE</h4>FREQUENTLY ASKED QUESTIONS<br>RETURN POLICY<br>CONTACT US</div>
  <div class="foot-col" style="left:440px"><h4>SUBSCRIBE FOR OUR NEWSLETTER</h4>
    <div class="newsletter-field"><span>Your email address</span><i></i></div>
    <div class="foot-call">CALL US +32 470 00 12 34</div></div>
  <div class="foot-bottom">© 2013 Lumo-Ward</div>
</footer>

</body>
</html>
```